Orrin Funeral Home stationery
Orrin Funeral Home
Professional
Duncan P. Orrin
Funeral Director
41 Larch St.
Calais, ME 04682
and
58 Mill St.
Eastport, ME 04657
207-516-2870 or 207-739-6152
duncan@orrinfuneralhome.example
www.orrinfuneralhome.example
The Eastport address is the 739 phone number
Logo
Funerals - Cremations - Prearrangements
Logo in eps

```html
<!DOCTYPE html>
<html lang="en">
<head>
<meta charset="utf-8">
<title>Orrin Funeral Home Stationery</title>
<link rel="stylesheet" href="https://fonts.googleapis.com/css2?family=Arimo:wght@400;700&family=Tinos:ital,wght@0,400;0,700;1,400&display=swap">
<style>
  :root {
    --bg: #e9e6e2;
    --paper: #ffffff;
    --navy: #1d3b8a;
    --blue: #2f5fc4;
    --blue-dark: #16307a;
    --tan: #c8b48c;
    --ink: #3a3f4a;
    --muted: #7a808c;
  }
  * { box-sizing: border-box; margin: 0; padding: 0; }
  html, body { width: 1200px; height: 897px; overflow: hidden; }
  body {
    background: var(--bg);
    font-family: "Arimo", Arial, sans-serif;
    color: var(--ink);
    position: relative;
  }
  .sheet {
    position: absolute;
    background: var(--paper);
    box-shadow: 0 2px 10px rgba(0,0,0,.12);
    overflow: hidden;
  }
  .brand { display: flex; align-items: center; gap: 8px; }
  .brand-dot {
    width: 14px; height: 14px; border-radius: 50%;
    background: var(--navy); flex: none;
  }
  .brand-name {
    font-family: "Tinos", "Times New Roman", serif;
    font-weight: 700; color: var(--navy);
    line-height: 1.05;
  }
  .rule-band {
    position: absolute; left: 0; right: 0; bottom: 0;
    background: linear-gradient(90deg, var(--blue-dark), var(--blue) 60%, var(--blue-dark));
    border-top: 3px solid var(--tan);
  }

  /* Letterhead */
  .letterhead { left: 70px; top: 150px; width: 460px; height: 600px; }
  .letterhead .brand { position: absolute; left: 34px; top: 30px; }
  .letterhead .brand-name { font-size: 19px; }
  .letter-body {
    position: absolute; left: 34px; top: 110px; right: 40px;
    font-size: 10px; line-height: 1.55; color: var(--ink);
  }
  .letter-body p { margin-bottom: 12px; }
  .letter-body .signoff { margin-top: 28px; }
  .letterhead .rule-band {
    height: 30px; color: #fff; font-size: 8.5px;
    display: flex; align-items: center; justify-content: center; letter-spacing: .2px;
  }

  /* Business card front */
  .card-front { left: 600px; top: 280px; width: 300px; height: 175px; }
  .card-front .brand { position: absolute; left: 16px; top: 16px; }
  .card-front .brand-name { font-size: 13px; }
  .card-front .person {
    position: absolute; right: 18px; top: 18px; text-align: right;
  }
  .person-name {
    font-family: "Tinos", "Times New Roman", serif;
    font-weight: 700; color: var(--navy); font-size: 17px;
  }
  .person-title { font-size: 9px; color: var(--muted); margin-top: 2px; }
  .card-front .contact {
    position: absolute; left: 16px; top: 64px;
    font-size: 8.5px; line-height: 1.45; color: var(--ink);
  }
  .card-front .rule-band { height: 18px; }

  /* Business card back */
  .card-back { left: 840px; top: 70px; width: 300px; height: 175px; border-radius: 12px; }
  .card-back .brand { position: absolute; left: 50%; top: 54px; transform: translateX(-50%); }
  .card-back .brand-name { font-size: 17px; white-space: nowrap; }
  .card-back .tagline {
    position: absolute; left: 0; right: 0; top: 104px; text-align: center;
    font-size: 8.5px; color: var(--muted); letter-spacing: .3px;
  }

  /* Envelope */
  .envelope { left: 600px; top: 510px; width: 540px; height: 250px; }
  .envelope .brand { position: absolute; left: 22px; top: 22px; }
  .envelope .brand-name { font-size: 15px; }
  .envelope .return {
    position: absolute; left: 22px; top: 62px;
    font-size: 8.5px; line-height: 1.45; color: var(--ink);
  }
  .envelope .top-line {
    position: absolute; left: 190px; right: 20px; top: 30px;
    height: 2px; background: var(--tan);
  }
  .envelope .rule-band { height: 20px; }
</style>
</head>
<body>

  <section class="sheet letterhead">
    <div class="brand"><span class="brand-dot"></span><span class="brand-name">Orrin Funeral Home</span></div>
    <div class="letter-body">
      <p>March 4, 2024</p>
      <p>Recipient Name<br>Street Address<br>City, State ZIP</p>
      <p>Dear Friend,</p>
      <p>Thank you for placing your trust in our family. We understand how difficult this time can be, and our staff is here to guide you through every arrangement with care, dignity and respect.</p>
      <p>Please call us at any hour with questions. We will gladly meet with you at either of our two locations.</p>
      <p class="signoff">Sincerely,<br><br>Duncan P. Orrin<br>Funeral Director</p>
    </div>
    <div class="rule-band">41 Larch St., Calais, ME 04682 &nbsp;·&nbsp; 58 Mill St., Eastport, ME 04657 &nbsp;·&nbsp; www.orrinfuneralhome.example</div>
  </section>

  <section class="sheet card-front">
    <div class="brand"><span class="brand-dot"></span><span class="brand-name">Orrin<br>Funeral Home</span></div>
    <div class="person">
      <div class="person-name">Duncan P. Orrin</div>
      <div class="person-title">Funeral Director</div>
    </div>
    <div class="contact">
      41 Larch St., Calais, ME 04682 &nbsp;·&nbsp; 207-516-2870<br>
      58 Mill St., Eastport, ME 04657 &nbsp;·&nbsp; 207-739-6152<br>
      duncan@orrinfuneralhome.example<br>
      www.orrinfuneralhome.example
    </div>
    <div class="rule-band"></div>
  </section>

  <section class="sheet card-back">
    <div class="brand"><span class="brand-dot"></span><span class="brand-name">Orrin Funeral Home</span></div>
    <div class="tagline">Funerals - Cremations - Prearrangements</div>
  </section>

  <section class="sheet envelope">
    <div class="brand"><span class="brand-dot"></span><span class="brand-name">Orrin Funeral Home</span></div>
    <div class="top-line"></div>
    <div class="return">
      41 Larch St.<br>
      Calais, ME 04682
    </div>
    <div class="rule-band"></div>
  </section>

</body>
</html>
```